Eye Popping Personal Finance Image Needed for Book Cover

We need an attention-grabbing and conceptually powerful image for the cover for the Go RichForm! book (see image for prototype cover). The image should represent the intersection of wealth and fitness, capturing the book's essence of building financial strength and freedom. The book is about getting your finances so you can position yourself to become wealthy (not physical fitness).

We specifically like the "money brain" as shown in The Quiet Logic of Coins book cover. (see image)

Key Elements to Include:
- RichForm theme represented through a fusion of wealth (money imagery) and fitness (exercise tools like the dumbbell).
- The design should evoke empowerment, strength, and the transformative journey of achieving financial freedom.

A possible angle COULD be a dumbbell made from rolled-up $100 US bills (instead of traditional weights). This symbolizes the idea of strengthening one's finances and creating wealth through discipline and effort. If you go this route you should ensure the dumbbell has a realistic yet stylized appearance, with a polished and professional look that feels aspirational.

Target Market(s)

See the PDF

Industry/Entity Type

personal finance

Colors

Designer to choose colors to be used in the design.

Requirements
Should not have
• euros, or other foreign currency

```html
<!DOCTYPE html>
<html lang="en">
<head>
<meta charset="utf-8">
<title>Go RichForm! – Book Cover</title>
<link rel="stylesheet" href="https://fonts.googleapis.com/css2?family=Anton&family=Montserrat:wght@800;900&display=swap">
<style>
  :root {
    --bg-deep: #14171e;
    --bg-mid: #2a2e37;
    --gold: #dcb97a;
    --gold-dark: #b08a48;
    --white: #ffffff;
    --frame: #e6e6e6;
    --brain-light: #6d7680;
    --brain-dark: #1b2027;
  }
  * { margin: 0; padding: 0; box-sizing: border-box; }
  html, body {
    width: 800px;
    height: 1200px;
    overflow: hidden;
    background: var(--bg-deep);
  }
  .cover {
    position: relative;
    width: 800px;
    height: 1200px;
    overflow: hidden;
    background:
      radial-gradient(ellipse 70% 45% at 50% 28%, var(--bg-mid) 0%, transparent 100%),
      radial-gradient(ellipse 60% 30% at 50% 82%, #262b34 0%, transparent 100%),
      var(--bg-deep);
  }
  .publisher-mark {
    position: absolute;
    top: 40px;
    right: 26px;
    display: flex;
    align-items: center;
    gap: 6px;
    font-family: "Montserrat", sans-serif;
    font-weight: 800;
    font-size: 13px;
    color: var(--gold);
  }
  .publisher-mark .dot {
    width: 12px;
    height: 12px;
    border-radius: 50%;
    background: var(--gold);
  }
  .cover-text {
    position: absolute;
    inset: 0;
  }
  .title {
    font-family: "Anton", sans-serif;
    fill: var(--gold);
    filter: drop-shadow(4px 6px 4px rgba(0,0,0,0.55));
  }
  .subtitle {
    font-family: "Montserrat", sans-serif;
    font-weight: 900;
  }
  .subtitle.white { fill: var(--white); }
  .subtitle.gold { fill: var(--gold); }
  .subtitle-frame {
    fill: none;
    stroke: var(--frame);
    stroke-width: 1;
  }
  .author {
    font-family: "Montserrat", sans-serif;
    font-weight: 900;
    fill: var(--white);
  }
  .money-brain {
    position: absolute;
    left: 84px;
    top: 643px;
    width: 590px;
    height: 495px;
    border-radius: 50% 50% 40% 45% / 58% 55% 40% 45%;
    background:
      radial-gradient(circle at 30% 35%, rgba(220,185,122,0.35) 0%, transparent 30%),
      radial-gradient(circle at 65% 60%, rgba(220,185,122,0.3) 0%, transparent 28%),
      radial-gradient(ellipse at 45% 35%, var(--brain-light) 0%, #3a424c 45%, var(--brain-dark) 100%);
    box-shadow: 0 30px 60px rgba(0,0,0,0.6);
  }
</style>
</head>
<body>
  <div class="cover">
    <div class="money-brain" role="img" aria-label="Illustration of a human brain built from dollar bills and gold dollar signs wrapped in a silver wire mesh"></div>

    <div class="publisher-mark"><span class="dot"></span>RichForm</div>

    <svg class="cover-text" width="800" height="1200" viewBox="0 0 800 1200">
      <text class="title" x="400" y="140" font-size="138" text-anchor="middle" textLength="142" lengthAdjust="spacingAndGlyphs">GO</text>
      <text class="title" x="97" y="286" font-size="183" textLength="620" lengthAdjust="spacingAndGlyphs">RICHFORM!</text>

      <rect class="subtitle-frame" x="94.5" y="304.5" width="624" height="314"/>
      <text class="subtitle white" x="258" y="349" font-size="27" textLength="289" lengthAdjust="spacing">ELIMINATE DEBT</text>
      <text class="subtitle white" x="127" y="411" font-size="66" textLength="557" lengthAdjust="spacing">BOOST YOUR</text>
      <text class="subtitle gold" x="127" y="505" font-size="113" textLength="557" lengthAdjust="spacing">INCOME</text>
      <text class="subtitle white" x="204" y="540" font-size="27" textLength="398" lengthAdjust="spacing">&amp; UNLOCK LONG-TERM</text>
      <text class="subtitle white" x="127" y="592" font-size="51" textLength="557" lengthAdjust="spacing">PASSIVE WEALTH</text>

      <text class="author" x="102" y="1184" font-size="59" textLength="598" lengthAdjust="spacing">DORIAN MATHESON</text>
    </svg>
  </div>
</body>
</html>
```